Industrial Professional Business Card Design (Vantrel Systems)

Would like professional looking business cards. Not too busy leaning towards minimal. Should have a slogan like:
"Industrial Automation and Control".

We are a tech company that programs industrial PLC computers. We also develop custom hardware solutions. Please use the logo for inspiration.

Target Market(s)

Mining, industrial, processing, automation, factory

Industry/Entity Type

Engineering

Contact Information for Business Card

Name, phone, email, website. job title.

Font styles to use
Other font styles liked:
• droid sans

Requirements
Must have
• Use colours that go well with the logo. Not too busy design.

```html
<!DOCTYPE html>
<html lang="en">
<head>
<meta charset="utf-8">
<title>Vantrel Systems — Business Card</title>
<link href="https://fonts.googleapis.com/css2?family=Noto+Sans:ital,wght@0,400;0,700;1,400&family=Roboto:wght@400&display=swap" rel="stylesheet">
<style>
  :root {
    --backdrop: #3b3b3d;
    --backdrop-dark: #2a2a2c;
    --card: #1f1f21;
    --card-edge: #151516;
    --silver: #9a9a9c;
    --blue: #2f8fc0;
    --blue-deep: #1d4f9a;
    --orange: #f06a1d;
    --white: #f2f2f2;
    --faint: rgba(255,255,255,0.035);
  }
  * { margin: 0; padding: 0; box-sizing: border-box; }
  html, body { width: 799px; height: 1200px; overflow: hidden; }
  body {
    background: radial-gradient(ellipse at 50% 40%, var(--backdrop), var(--backdrop-dark));
    font-family: "Noto Sans", Arial, sans-serif;
    position: relative;
  }
  .card {
    position: absolute;
    left: 90px;
    width: 620px;
    height: 354px;
    background: var(--card);
    border-radius: 4px;
    box-shadow: 0 14px 30px rgba(0,0,0,0.55);
    overflow: hidden;
  }
  .card-front { top: 120px; }
  .card-back { top: 700px; }

  /* Front */
  .front-brand {
    position: absolute;
    inset: 0;
    display: flex;
    align-items: center;
    justify-content: center;
    gap: 18px;
  }
  .brand-dot {
    width: 64px; height: 64px;
    border-radius: 50%;
    background: #2b2b2d;
  }
  .front-name {
    font-size: 44px;
    font-weight: 400;
    color: var(--silver);
    letter-spacing: 0.5px;
  }

  /* Back */
  .side-band {
    position: absolute;
    left: 0; top: 0; bottom: 0;
    width: 42px;
    background: linear-gradient(180deg, var(--blue), var(--blue-deep));
  }
  .side-rule {
    position: absolute;
    left: 50px; top: 0; bottom: 0;
    width: 4px;
    background: var(--orange);
  }
  .faint-circle {
    position: absolute;
    right: -40px; top: 110px;
    width: 300px; height: 300px;
    border-radius: 50%;
    background: var(--faint);
  }
  .back-brand {
    position: absolute;
    left: 84px; top: 38px;
    display: flex; align-items: center; gap: 16px;
  }
  .back-brand .brand-dot { width: 60px; height: 60px; background: var(--orange); }
  .back-name {
    font-size: 40px;
    font-weight: 400;
    color: var(--blue);
  }
  .person { position: absolute; left: 84px; top: 138px; }
  .person-name { font-size: 21px; font-weight: 700; color: var(--blue); }
  .person-title { font-size: 14px; font-style: italic; color: var(--white); margin-top: 2px; }
  .address {
    position: absolute; left: 84px; top: 210px;
    font-family: "Roboto", Arial, sans-serif;
    font-size: 15px; line-height: 1.45; color: var(--white);
  }
  .contact {
    position: absolute; left: 330px; top: 255px;
    list-style: none;
    font-family: "Roboto", Arial, sans-serif;
    font-size: 15px; color: var(--white);
  }
  .contact li { display: flex; align-items: center; gap: 14px; line-height: 26px; }
  .contact svg { width: 13px; height: 13px; fill: var(--orange); flex: none; }
</style>
</head>
<body>

<section class="card card-front" aria-label="Card front">
  <div class="front-brand">
    <span class="brand-dot"></span>
    <span class="front-name">Vantrel Systems</span>
  </div>
</section>

<section class="card card-back" aria-label="Card back">
  <div class="side-band"></div>
  <div class="side-rule"></div>
  <div class="faint-circle"></div>

  <div class="back-brand">
    <span class="brand-dot"></span>
    <span class="back-name">Vantrel Systems</span>
  </div>

  <div class="person">
    <p class="person-name">Daniel Reyes</p>
    <p class="person-title">Managing Director</p>
  </div>

  <p class="address">58 Foundry Rd., Millbrook,<br>Ashford, US 204815</p>

  <ul class="contact">
    <li>
      <svg viewBox="0 0 24 24" aria-hidden="true"><path d="M6.6 10.8a15 15 0 0 0 6.6 6.6l2.2-2.2c.3-.3.7-.4 1-.2 1.1.4 2.3.6 3.6.6.6 0 1 .4 1 1V20c0 .6-.4 1-1 1A17 17 0 0 1 3 4c0-.6.4-1 1-1h3.5c.6 0 1 .4 1 1 0 1.3.2 2.5.6 3.6.1.3 0 .7-.2 1z"/></svg>
      555-014-2290
    </li>
    <li>
      <svg viewBox="0 0 24 24" aria-hidden="true"><path d="M2 5h20v14H2z M2 5l10 8 10-8" stroke="#1f1f21" stroke-width="1.5"/></svg>
      daniel@vantrelsys.com
    </li>
    <li>
      <svg viewBox="0 0 24 24" aria-hidden="true"><circle cx="12" cy="12" r="10"/><path d="M2 12h20M12 2c3 3 3 17 0 20M12 2c-3 3-3 17 0 20" stroke="#1f1f21" stroke-width="1.4" fill="none"/></svg>
      www.vantrelsys.com
    </li>
  </ul>
</section>

</body>
</html>
```